IT Company based on Biology Business Needs a Business Card Design

We need a business card design for a new company called 'Lumen CELL'. We develop the machine learning solutions especially focused on deep learning algorithms for biology industry. Our initial product is a vision detection on biological images to help doctors diagnose the symptoms. We would like to see designs that use the color green.

Industry/Entity Type

Business

```html
<!DOCTYPE html>
<html lang="en">
<head>
<meta charset="utf-8">
<title>Lumen CELL — Business Card</title>
<link rel="stylesheet" href="https://fonts.googleapis.com/css2?family=Montserrat:wght@600&family=Open+Sans:wght@400;600&display=swap">
<style>
  :root {
    --green: #1a8a45;
    --green-light: #6cc04a;
    --white: #ffffff;
    --stage: #2b2b2b;
    --ring: rgba(255, 255, 255, 0.85);
  }
  html, body {
    margin: 0;
    width: 1200px;
    height: 900px;
    overflow: hidden;
    background: var(--stage);
    font-family: "Open Sans", sans-serif;
  }
  .card {
    position: absolute;
    width: 700px;
    height: 400px;
    border-radius: 18px;
    overflow: hidden;
    background: var(--white);
    box-shadow: 0 10px 30px rgba(0, 0, 0, 0.45);
  }
  .card--back { left: 60px; top: 40px; }
  .card--front { left: 440px; top: 460px; }

  /* back */
  .back-field {
    position: absolute;
    left: 0; right: 0; top: 14px; bottom: 14px;
    background: var(--green);
  }
  .brand {
    position: absolute;
    display: flex;
    align-items: center;
    gap: 16px;
    font-family: "Montserrat", sans-serif;
    font-weight: 600;
    letter-spacing: -1px;
    white-space: nowrap;
  }
  .brand__dot {
    border-radius: 50%;
    flex: none;
  }
  .card--back .brand {
    left: 170px; top: 160px;
    font-size: 60px;
    color: var(--white);
  }
  .card--back .brand__dot { width: 44px; height: 44px; background: var(--white); }

  /* front */
  .front-band {
    position: absolute;
    left: 0; right: 0; top: 190px; bottom: 14px;
    background: var(--green);
  }
  .holder {
    position: absolute;
    right: 40px; top: 30px;
    text-align: center;
    color: var(--green-light);
  }
  .holder__name { font-size: 22px; font-weight: 600; letter-spacing: 0.5px; }
  .holder__title { font-size: 12px; color: var(--green); }
  .card--front .brand {
    left: 60px; top: 88px;
    font-size: 50px;
    color: var(--green-light);
  }
  .card--front .brand__dot { width: 36px; height: 36px; background: var(--green); }

  .contact {
    position: absolute;
    top: 210px;
    width: 200px;
    text-align: center;
    color: var(--white);
    font-size: 14px;
    line-height: 1.45;
  }
  .contact--phone { left: 30px; }
  .contact--web { left: 250px; }
  .contact--place { left: 470px; }
  .contact__ring {
    width: 104px; height: 104px;
    margin: 0 auto 14px;
    display: block;
  }
</style>
</head>
<body>

<section class="card card--back" aria-label="Card back">
  <div class="back-field"></div>
  <div class="brand"><span class="brand__dot"></span>Lumen CELL</div>
</section>

<section class="card card--front" aria-label="Card front">
  <div class="front-band"></div>

  <div class="holder">
    <div class="holder__name">Your Name</div>
    <div class="holder__title">Title</div>
  </div>

  <div class="brand"><span class="brand__dot"></span>Lumen CELL</div>

  <div class="contact contact--phone">
    <svg class="contact__ring" viewBox="0 0 104 104" aria-hidden="true">
      <circle cx="52" cy="52" r="50" fill="none" stroke="var(--ring)" stroke-width="1.5" stroke-dasharray="3 4"/>
      <circle cx="52" cy="52" r="9" fill="none" stroke="#fff" stroke-width="1.8"/>
      <path d="M48.5 47.5c1 3 2.6 5.2 5 6.6l1.6-1.4 2 1.2-.8 2c-3.8 0-8.7-4.6-9-8.6l2-.8z" fill="#fff"/>
    </svg>
    555.010.2525<br>555.010.2514
  </div>

  <div class="contact contact--web">
    <svg class="contact__ring" viewBox="0 0 104 104" aria-hidden="true">
      <circle cx="52" cy="52" r="50" fill="none" stroke="var(--ring)" stroke-width="1.5" stroke-dasharray="3 4"/>
      <g fill="none" stroke="#fff" stroke-width="1.6">
        <circle cx="52" cy="52" r="11"/>
        <ellipse cx="52" cy="52" rx="5" ry="11"/>
        <path d="M41 52h22M43 46h18M43 58h18"/>
      </g>
    </svg>
    name@yourweb.com<br>www.yourweb.com
  </div>

  <div class="contact contact--place">
    <svg class="contact__ring" viewBox="0 0 104 104" aria-hidden="true">
      <circle cx="52" cy="52" r="50" fill="none" stroke="var(--ring)" stroke-width="1.5" stroke-dasharray="3 4"/>
      <path d="M52 64c-5-7-8-11-8-15a8 8 0 0 1 16 0c0 4-3 8-8 15z" fill="#fff"/>
      <circle cx="52" cy="49" r="3" fill="var(--green)"/>
    </svg>
    Your Office address<br>in Just Two Line
  </div>
</section>

</body>
</html>
```